Flyer-Design für Tierphysiotherapie und Osteopathie
Zielgruppe
Tierphysiotherapie und Osteopathie Lotte Brenner
Aufgabenstellung
Text des gewünschten Flyers ist hochgeladen.
Ebenso die Visitenkarten und das Logo, sowie die Website - zur Orientierung von Farben, Schriftarten, etc.
Auch ein paar Bilder sind beigefügt.

```html
<!DOCTYPE html>
<html lang="de">
<head>
<meta charset="utf-8">
<title>Flyer Tierphysiotherapie Lotte Brenner</title>
<link href="https://fonts.googleapis.com/css2?family=Dosis:wght@400;500;700;800&display=swap" rel="stylesheet">
<style>
:root{
  --yellow:#f0b622;
  --yellow-soft:#f5c94f;
  --ink:#2e2e2e;
  --grey:#6d6d6d;
  --paper:#ffffff;
  --stage:#f2f2f2;
}
*{box-sizing:border-box;margin:0;padding:0}
html,body{width:1200px;height:817px;overflow:hidden;background:var(--stage);font-family:'Dosis',sans-serif;color:var(--ink)}
.canvas{position:relative;width:1200px;height:817px}
.flyer{position:absolute;top:30px;width:360px;height:757px;background:var(--paper);overflow:hidden;box-shadow:0 4px 14px rgba(0,0,0,.12)}
.flyer--front{left:225px}
.flyer--back{left:615px}
.abs{position:absolute}

/* front */
.front-photo{left:0;top:0;width:360px;height:390px;background:linear-gradient(160deg,#4f7a3a 0%,#8a5a32 40%,#b5773f 60%,#6d9a4a 100%)}
.front-header{left:0;top:0}
.brand{display:flex;align-items:center;gap:8px;font-family:'Dosis',sans-serif;font-weight:500;color:var(--grey);font-size:17px;line-height:1.15}
.brand-dot{width:14px;height:14px;border-radius:50%;background:var(--yellow);flex:none}
.front-brand{left:120px;top:40px}
.front-badge{right:-14px;top:290px;width:190px;background:var(--yellow);border-radius:18px;padding:10px 22px 10px 16px;color:#fff;font-weight:700;font-size:21px;line-height:1.12;text-align:center;box-shadow:0 3px 8px rgba(0,0,0,.15)}
.want-title{left:24px;top:420px;color:var(--yellow);font-weight:800;font-size:20px}
.want-list{left:24px;top:450px;width:320px;list-style:none;font-size:12.5px;line-height:1.32}
.want-list li{display:flex;gap:7px;margin-bottom:7px}
.tick{flex:none;width:15px;height:15px;margin-top:1px}
.front-cta{left:0;bottom:0;width:360px;height:56px;background:var(--yellow);color:#fff;font-weight:800;font-size:20px;display:flex;align-items:center;justify-content:center}

/* back */
.back-photo{left:0;top:0;width:360px;height:170px;background:linear-gradient(120deg,#3b2f26 0%,#6a4a33 50%,#8a8f98 75%,#4b3a2c 100%)}
.back-badge{left:-6px;top:70px;width:170px;background:var(--yellow-soft);border-radius:0 16px 16px 0;padding:10px 10px 10px 20px;color:#fff;font-size:12.5px;line-height:1.5;text-align:center}
.back-badge b{font-weight:700}
.back-body{left:26px;top:196px;width:312px;font-size:12px;line-height:1.38}
.back-body p{margin-bottom:12px}
.accent{color:var(--yellow);font-weight:700}
.therapy-list{left:22px;top:310px;width:140px;list-style:none;font-size:12px;line-height:1.3}
.therapy-list li{display:flex;gap:7px;margin-bottom:9px}
.therapy-photo{left:176px;top:308px;width:164px;height:140px;border-radius:14px;background:linear-gradient(170deg,#8fae6a 0%,#5d8a3c 55%,#6b8fb3 80%,#4f3a2c 100%)}
.promise{left:0;top:470px;width:360px;height:112px;background:var(--yellow);color:#fff;text-align:center;padding:12px 18px;font-weight:700}
.promise-lead{font-size:11.5px;line-height:1.35}
.promise-claim{font-size:14.5px;line-height:1.22;margin-top:8px;font-weight:800}
.appointment{left:26px;top:596px;width:315px;font-size:11.5px;line-height:1.4}
.appointment strong{font-weight:800}
.back-brand{left:26px;top:675px;font-size:14px}
.contact{right:10px;top:658px;width:170px;height:78px;background:var(--yellow);color:#fff;font-weight:700;font-size:12px;line-height:1.6;padding:10px 14px;display:flex;flex-direction:column;justify-content:center}
</style>
</head>
<body>
<main class="canvas">

  <section class="flyer flyer--front" aria-label="Flyer Vorderseite">
    <div class="abs front-photo" role="img" aria-label="Foto: Therapeutin behandelt das Vorderbein eines Haflinger-Pferdes auf der Weide"></div>
    <svg class="abs front-header" width="360" height="400" viewBox="0 0 360 400" aria-hidden="true">
      <path d="M100 0 H360 V70 C300 110 200 120 150 100 C120 85 105 50 100 0 Z" fill="var(--paper)"/>
      <path d="M150 100 C200 120 300 110 360 70 V80 C300 122 200 130 150 100 Z" fill="var(--yellow)"/>
      <path d="M100 0 C105 50 120 85 150 100" fill="none" stroke="var(--yellow)" stroke-width="6"/>
      <path d="M0 390 C120 360 250 355 360 350 V400 H0 Z" fill="var(--paper)"/>
      <path d="M0 390 C120 360 250 355 360 350 V356 C250 361 120 368 0 396 Z" fill="var(--yellow)"/>
    </svg>
    <div class="abs brand front-brand"><span class="brand-dot"></span><span>Tierphysiotherapie<br>Lotte Brenner</span></div>
    <div class="abs front-badge">Lotte Brenner<br>Tierphysiotherapie<br>und Osteopathie</div>

    <h2 class="abs want-title">Sie möchten:</h2>
    <ul class="abs want-list">
      <li><svg class="tick" viewBox="0 0 16 16"><circle cx="8" cy="8" r="6.5" fill="none" stroke="var(--yellow)" stroke-width="1.6"/><path d="M4.5 8.2l2.4 2.4L13 3.5" fill="none" stroke="var(--yellow)" stroke-width="1.8"/></svg><span>Ihrem Jungtier einen guten Start ins Leben ermöglichen?</span></li>
      <li><svg class="tick" viewBox="0 0 16 16"><circle cx="8" cy="8" r="6.5" fill="none" stroke="var(--yellow)" stroke-width="1.6"/><path d="M4.5 8.2l2.4 2.4L13 3.5" fill="none" stroke="var(--yellow)" stroke-width="1.8"/></svg><span>Ihr Tier langfristig fit erhalten, um bis ins hohe Alter Freude an gemeinsamen Unternehmungen zu haben?</span></li>
      <li><svg class="tick" viewBox="0 0 16 16"><circle cx="8" cy="8" r="6.5" fill="none" stroke="var(--yellow)" stroke-width="1.6"/><path d="M4.5 8.2l2.4 2.4L13 3.5" fill="none" stroke="var(--yellow)" stroke-width="1.8"/></svg><span>bei Beschwerden im Bewegungsapparat wie Arthrose, Bandscheibenvorfällen oder neurologischen Erkrankungen oder nach Verletzungen oder Operationen kompetent und mit Feingefühl unterstützt werden?</span></li>
      <li><svg class="tick" viewBox="0 0 16 16"><circle cx="8" cy="8" r="6.5" fill="none" stroke="var(--yellow)" stroke-width="1.6"/><path d="M4.5 8.2l2.4 2.4L13 3.5" fill="none" stroke="var(--yellow)" stroke-width="1.8"/></svg><span>Ihren Sportler professionell begleiten lassen?</span></li>
      <li><svg class="tick" viewBox="0 0 16 16"><circle cx="8" cy="8" r="6.5" fill="none" stroke="var(--yellow)" stroke-width="1.6"/><path d="M4.5 8.2l2.4 2.4L13 3.5" fill="none" stroke="var(--yellow)" stroke-width="1.8"/></svg><span>Durch regelmäßigen Check Up, frühzeitig erkennen, wo doch mal was zwickt oder klemmt?</span></li>
    </ul>
    <div class="abs front-cta">Dann sind Sie bei mir richtig!</div>
  </section>

  <section class="flyer flyer--back" aria-label="Flyer Rückseite">
    <div class="abs back-photo" role="img" aria-label="Foto: Therapeutin sitzt mit zwei Möpsen vor einer Scheune"></div>
    <svg class="abs" style="left:0;top:150px" width="360" height="40" viewBox="0 0 360 40" aria-hidden="true">
      <path d="M0 20 C120 36 260 34 360 18 V40 H0 Z" fill="var(--paper)"/>
      <path d="M0 14 C120 30 260 28 360 12 V18 C260 34 120 36 0 20 Z" fill="var(--yellow)"/>
    </svg>
    <div class="abs back-badge">Ich heiße <b>Lotte Brenner</b><br>und bin <b>Physiotherapeutin</b><br><b>und Osteopathin</b> für Tiere</div>

    <div class="abs back-body">
      <p>Einschränkungen, Blockaden oder Schmerzen können viele Ursachen haben und äußern sich bei jedem Tier anders. Ihr Tier ist einzigartig, deshalb bekommen Sie bei mir die Behandlung, die zu Ihrem Tier und Ihnen passt!</p>
      <p>Neben der Arbeit mit meinen Händen biete ich unterschiedliche <span class="accent">Therapieformen und Leistungen</span> an wie z.b.</p>
    </div>
    <ul class="abs therapy-list">
      <li><svg class="tick" viewBox="0 0 16 16"><circle cx="8" cy="8" r="6.5" fill="none" stroke="var(--yellow)" stroke-width="1.6"/><path d="M4.5 8.2l2.4 2.4L13 3.5" fill="none" stroke="var(--yellow)" stroke-width="1.8"/></svg><span>Lasertherapie</span></li>
      <li><svg class="tick" viewBox="0 0 16 16"><circle cx="8" cy="8" r="6.5" fill="none" stroke="var(--yellow)" stroke-width="1.6"/><path d="M4.5 8.2l2.4 2.4L13 3.5" fill="none" stroke="var(--yellow)" stroke-width="1.8"/></svg><span>Neurostim</span></li>
      <li><svg class="tick" viewBox="0 0 16 16"><circle cx="8" cy="8" r="6.5" fill="none" stroke="var(--yellow)" stroke-width="1.6"/><path d="M4.5 8.2l2.4 2.4L13 3.5" fill="none" stroke="var(--yellow)" stroke-width="1.8"/></svg><span>aktives und passives Bewegungstraining</span></li>
      <li><svg class="tick" viewBox="0 0 16 16"><circle cx="8" cy="8" r="6.5" fill="none" stroke="var(--yellow)" stroke-width="1.6"/><path d="M4.5 8.2l2.4 2.4L13 3.5" fill="none" stroke="var(--yellow)" stroke-width="1.8"/></svg><span>gezielter Muskelaufbau</span></li>
      <li><svg class="tick" viewBox="0 0 16 16"><circle cx="8" cy="8" r="6.5" fill="none" stroke="var(--yellow)" stroke-width="1.6"/><path d="M4.5 8.2l2.4 2.4L13 3.5" fill="none" stroke="var(--yellow)" stroke-width="1.8"/></svg><span>und vieles mehr</span></li>
    </ul>
    <div class="abs therapy-photo" role="img" aria-label="Foto: Therapeutin behandelt einen Hund auf einer Decke im Gras"></div>

    <div class="abs promise">
      <p class="promise-lead">Ich gehe ganz besonders auf die speziellen Bedürfnisse Ihres Tiere ein. Und begleite Sie und Ihr Tier liebevoll und einfühlsam</p>
      <p class="promise-claim">Gemeinsam finden wir den besten Weg zu mehr Bewegung und Lebensfreude!</p>
    </div>
    <p class="abs appointment">Termine für Hunde und Kleintiere finden nach Vereinbarung in meiner Praxis in <strong>71634 Lindenfeld, Am Wiesenhang 7 statt</strong>.<br>Ich freue mich auf Sie</p>
    <div class="abs brand back-brand"><span class="brand-dot"></span><span>Tierphysiotherapie<br>Lotte Brenner</span></div>
    <div class="abs contact">
      <span>info@tierphysio-brenner.de</span>
      <span>0160/2837415</span>
      <span>www.tierphysio-brenner.de</span>
    </div>
  </section>

</main>
</body>
</html>
```